Need Letterhead & Stationery for Construction Company

Hello,
I have a small construction company that I recently started. I already have the logo but I want to create a letterhead, stationery and business cards for it. I want an elegant design which should feel like a corporate company. Kindly let me know what else you need from my end to start with the design.
I also need digital copies of letterhead so that I can send PDF's directly to clients.

** logo attached, colors I would like to stay in Grey / Shades of Red

** Details required in Business Card:
Name, Designation, Mobile, Telephone, Email, other email, POBOX, Address, website

Requirements
Should not have
• funky styles, too many colors.

```html
<!DOCTYPE html>
<html lang="en">
<head>
<meta charset="utf-8">
<title>Arden Steel – Letterhead</title>
<link rel="stylesheet" href="https://fonts.googleapis.com/css2?family=Montserrat:wght@500;700;800&family=Roboto:wght@400;500&display=swap">
<style>
  :root {
    --red: #e3262c;
    --red-deep: #b8141c;
    --red-soft: #f36a5a;
    --grey: #d9d9db;
    --grey-mid: #b9b9bc;
    --ink: #1d1d1f;
    --text: #4a4a4d;
    --paper: #ffffff;
    --watermark: #fbe3d8;
  }
  * { margin: 0; padding: 0; box-sizing: border-box; }
  html, body { width: 849px; height: 1200px; overflow: hidden; background: var(--paper); }
  .letterhead { position: relative; width: 849px; height: 1200px; background: var(--paper); overflow: hidden; }

  .corner { position: absolute; display: block; }
  .corner--top { top: 0; right: 0; }
  .corner--bottom { bottom: 0; left: 0; }

  .brand { position: absolute; top: 34px; left: 28px; display: flex; align-items: center; gap: 12px; }
  .brand__dot { width: 74px; height: 74px; border-radius: 50%; background: var(--ink); }
  .brand__text { display: flex; flex-direction: column; }
  .brand__name {
    font-family: "Montserrat", sans-serif; font-weight: 800; font-size: 50px;
    letter-spacing: 9px; color: var(--ink); line-height: 1;
  }
  .brand__tagline {
    font-family: "Montserrat", sans-serif; font-weight: 700; font-size: 11.5px;
    letter-spacing: 0.6px; color: var(--ink); margin-top: 6px;
  }

  .watermark {
    position: absolute; top: 520px; left: 0; width: 849px; text-align: center;
    font-family: "Montserrat", sans-serif; font-weight: 800; font-size: 150px;
    letter-spacing: 10px; color: var(--watermark); line-height: 1;
  }

  .contact {
    position: absolute; right: 26px; top: 1022px;
    font-family: "Roboto", sans-serif; font-size: 13px; color: var(--text);
    text-align: right; line-height: 17px;
  }
  .contact__row { display: flex; justify-content: flex-end; align-items: center; gap: 12px; margin-bottom: 18px; }
  .contact__icon {
    width: 22px; height: 22px; border-radius: 3px; background: var(--red);
    display: flex; align-items: center; justify-content: center; flex: none;
  }
  .contact__icon svg { width: 13px; height: 13px; fill: #fff; }
</style>
</head>
<body>
<main class="letterhead">

  <svg class="corner corner--top" width="330" height="120" viewBox="0 0 330 120" aria-hidden="true">
    <defs>
      <linearGradient id="redTop" x1="0" y1="0" x2="1" y2="1">
        <stop offset="0" stop-color="var(--red-soft)"/>
        <stop offset="1" stop-color="var(--red-deep)"/>
      </linearGradient>
    </defs>
    <polygon points="60,0 330,0 330,30" fill="var(--grey)"/>
    <polygon points="150,0 330,0 330,112" fill="url(#redTop)"/>
    <polygon points="230,0 330,0 330,60" fill="var(--red-deep)"/>
    <polygon points="115,0 175,0 215,45" fill="var(--red)"/>
  </svg>

  <header class="brand">
    <span class="brand__dot"></span>
    <div class="brand__text">
      <span class="brand__name">ARDEN</span>
      <span class="brand__tagline">STEEL CONSTRUCTIONS CONTRACTING LLC</span>
    </div>
  </header>

  <div class="watermark" aria-hidden="true">ARDEN</div>

  <address class="contact">
    <div class="contact__row">
      <span>(+971)4-000 5120</span>
      <span class="contact__icon"><svg viewBox="0 0 24 24"><path d="M6.6 10.8a15.1 15.1 0 0 0 6.6 6.6l2.2-2.2c.3-.3.7-.4 1-.2 1.1.4 2.3.6 3.6.6.6 0 1 .4 1 1V20c0 .6-.4 1-1 1A17 17 0 0 1 3 4c0-.6.4-1 1-1h3.5c.6 0 1 .4 1 1 0 1.3.2 2.5.6 3.6.1.3 0 .7-.2 1z"/></svg></span>
    </div>
    <div class="contact__row">
      <span>info@ardensteel.ae<br>www.ardensteel.ae</span>
      <span class="contact__icon"><svg viewBox="0 0 24 24"><circle cx="12" cy="12" r="9" fill="none" stroke="#fff" stroke-width="2"/><path d="M3 12h18M12 3c3 3 3 15 0 18M12 3c-3 3-3 15 0 18" fill="none" stroke="#fff" stroke-width="1.6"/></svg></span>
    </div>
    <div class="contact__row">
      <span>Office 904, Harbor Point<br>Canal Street, Business Bay, Dubai (U.A.E)</span>
      <span class="contact__icon"><svg viewBox="0 0 24 24"><path d="M12 2a7 7 0 0 0-7 7c0 5.2 7 13 7 13s7-7.8 7-13a7 7 0 0 0-7-7zm0 9.5A2.5 2.5 0 1 1 12 6.5a2.5 2.5 0 0 1 0 5z"/></svg></span>
    </div>
    <div class="contact__row">
      <span>POBox: 52817</span>
      <span class="contact__icon"><svg viewBox="0 0 24 24"><path d="M3 6h18v12H3z"/><path d="M3 6l9 7 9-7" fill="none" stroke="var(--red)" stroke-width="1.8"/></svg></span>
    </div>
  </address>

  <svg class="corner corner--bottom" width="360" height="170" viewBox="0 0 360 170" aria-hidden="true">
    <defs>
      <linearGradient id="redBottom" x1="0" y1="0" x2="1" y2="1">
        <stop offset="0" stop-color="var(--red-deep)"/>
        <stop offset="1" stop-color="var(--red-soft)"/>
      </linearGradient>
    </defs>
    <polygon points="0,60 220,170 0,170" fill="var(--grey)"/>
    <polygon points="0,0 170,170 0,170" fill="url(#redBottom)"/>
    <polygon points="0,95 110,170 0,170" fill="var(--red-deep)"/>
    <polygon points="90,128 360,170 150,170" fill="var(--red)"/>
    <polygon points="200,150 300,170 240,170" fill="var(--grey-mid)"/>
  </svg>

</main>
</body>
</html>
```